Float and wellness centre needs a website refresh

Our float and wellness centre has been operating in Brisbane, Australia for 3 months. Our website is functional and easy to use, but it lacks a compelling visual experience that sells our awesome services to our customers.<br/><br/>We would like a complete redesign of our webpage. It is very important that the redesign considers the page layout for mobile users and the winning design will need to show both a desktop and mobile version of each of the pages listed below.<br/><br/>Out current website can be found at https://www.ebbtidehaven.com.au/<br/><br/>The winning design will need to provide proposals for redesigning the 4 pages listed below:<br/>Home Page - https://www.ebbtidehaven.com.au/<br/>Float Page - https://www.ebbtidehaven.com.au/services/float<br/>Build Gift Card page - https://www.ebbtidehaven.com.au/giftcard/stepone?location=kelsworth<br/>Booking Page - https://www.ebbtidehaven.com.au/Calendar/Day?centerId=kelsworth&selectedCategory=FLOAT&date=12/18/2019%2000:00:00%20+10:00&sessionLength=60<br/><br/>We only need the 4 pages listed above as our web developer will use the assets from the above pages to standardize all the other pages in the site. It is very important your proposed pages contain the same information as our current pages so that we can properly see the complete layout.<br/><br/>The Home page must display the business logo in some way. We would like the website to have a white background and for it make tasteful use of color to highlight key features on the pages. Where color is used it should harmonize with the business logo. The website needs to feel bright, simple and relaxing. Our current site does not use images very well and we have had professional photos taken of the center and the float rooms specifically for this website project. You can download these, and the business logo images here: http://ebbtidehaven.com.au/websiteimages.zip <br/><br/>We have included a few links below to other centers who have pages that we like: <br/><br/>https://www.drifthollowpods.com/ <br/>https://www.quietnook.com.au/ <br/>https://www.moonbaysoak.com.au/<br/>

Industry/Entity Type

Health And Wellness

Number of Pages Required

4 page

Font styles to use
Sans Serif

Colors

Designer to choose colors to be used in the design.

Requirements
Must have
• It is very important your proposed pages contain the same information as our current pages so that we can properly see the complete layout.
• The Home page must display the business logo in some way.
• Where color is used it should harmonize with the business logo.
Nice to have
• The website needs to feel bright, simple and relaxing. Our current site does not use images very well and we have had professional photos taken of the center and the float rooms specifically for this website project. You can download these, and the business logo images here: http://ebbtidehaven.com.au/websiteimages.zip
Should not have
• Dark pages.

```html
<!DOCTYPE html>
<html lang="en">
<head>
<meta charset="utf-8">
<title>Ebbtide Haven – Wellness Spa</title>
<link href="https://fonts.googleapis.com/css2?family=Roboto:wght@300;400;500;700&display=swap" rel="stylesheet">
<style>
:root{
  --teal:#12a6b4;
  --ink:#3b3b3b;
  --text:#333;
  --dark:#3f3f3f;
  --white:#fff;
  --line:#444;
  --foot-text:#eeeeee;
}
*{box-sizing:border-box;margin:0;padding:0}
html,body{width:1200px;height:2557px;overflow:hidden;background:var(--white);font-family:'Roboto',sans-serif;color:var(--text)}
.page{position:relative;width:1200px;height:2557px}

/* header */
.site-header{position:absolute;left:0;top:0;width:1200px;height:77px;background:var(--white)}
.brand{position:absolute;left:153px;top:25px;display:flex;align-items:center;gap:8px;font-size:20px;font-weight:300;color:#555}
.brand-dot{width:26px;height:26px;border-radius:50%;background:var(--teal)}
.main-nav{position:absolute;left:376px;top:31px;display:flex;font-size:14px;color:#444}
.main-nav span{margin-right:37px}
.btn-teal{background:var(--teal);color:var(--white);font-size:14px;font-weight:500;display:flex;align-items:center;justify-content:center}
.header-book{position:absolute;left:932px;top:22px;width:117px;height:34px}

/* hero */
.hero{position:absolute;left:0;top:77px;width:1200px;height:559px;
  background:
    radial-gradient(ellipse 360px 130px at 600px 300px,rgba(38,92,112,.85),rgba(38,92,112,0) 100%),
    linear-gradient(90deg,#efe6d2 0%,#f3ecdc 20%,#f6f1e6 50%,#f1ebdf 80%,#ece9e6 100%);}
.hero::after{content:"";position:absolute;left:0;right:0;bottom:0;height:200px;background:linear-gradient(180deg,rgba(210,200,184,0),#cfc2ab 70%,#bfb3a0)}
.hero-title,.hero-sub,.hero-book{z-index:1;text-shadow:0 1px 8px rgba(40,50,55,.45)}
.hero-title{position:absolute;left:0;width:1200px;top:158px;text-align:center;font-size:60px;font-weight:500;color:var(--white)}
.hero-sub{position:absolute;left:0;width:1190px;top:236px;text-align:center;font-size:15px;font-weight:500;color:var(--white)}
.hero-book{position:absolute;left:542px;top:318px;width:116px;height:33px;border:2px solid var(--white);color:var(--white);font-size:14px;display:flex;align-items:center;justify-content:center;background:rgba(40,70,80,.15)}

/* about */
.section-title{font-size:30px;font-weight:500;color:var(--ink)}
.rule{width:61px;height:3px;background:var(--teal)}
.about-title{position:absolute;left:152px;top:736px}
.about-rule{position:absolute;left:152px;top:782px}
.mission-head{position:absolute;left:152px;top:814px;font-size:15px;font-weight:500;color:#333}
.mission-text{position:absolute;left:152px;width:382px;font-size:11px;font-weight:300;line-height:13.5px;color:#222}
.pod-frame{position:absolute;left:740px;top:692px;width:309px;height:308px;border:3px solid var(--line)}
.pod-photo{position:absolute;left:657px;top:722px;width:373px;height:218px;border-radius:36px;
  background:radial-gradient(ellipse at 45% 30%,#ffffff 0%,#f6f8fb 45%,#e3e8ee 85%,#d3dae2 100%)}

/* service slider */
.slide-photo{position:absolute;left:209px;top:1059px;width:472px;height:417px;
  background:
    radial-gradient(ellipse 190px 110px at 240px 270px,#2f86e6 0%,#4c9cf0 45%,rgba(120,170,230,0) 100%),
    linear-gradient(180deg,#f4efe6 0%,#f1ece3 45%,#e8e6e2 100%)}
.slide-panel{position:absolute;left:681px;top:1059px;width:312px;height:417px;background:var(--dark);color:var(--white);text-align:center}
.slide-panel h3{font-size:30px;font-weight:500;margin-top:56px}
.slide-panel .len{font-size:20px;margin-top:6px}
.slide-panel .sess{font-size:11px;line-height:13px;margin-top:7px}
.slide-panel .price{font-size:30px;margin-top:26px}
.slide-book{display:inline-flex;margin-top:22px;width:117px;height:33px;background:var(--white);color:var(--ink);font-size:14px;align-items:center;justify-content:center}
.arrow{position:absolute;width:52px;height:52px}

/* gallery */
.gallery-title{position:absolute;left:0;width:1200px;top:1528px;text-align:center}
.gallery-rule{position:absolute;left:569px;top:1574px}
.gallery{position:absolute;left:55px;top:1605px;width:1093px;display:grid;grid-template-columns:repeat(4,267px);grid-auto-rows:266px;gap:9px}
.show-more{position:absolute;left:541px;top:2172px;width:117px;height:33px}

/* footer */
.site-footer{position:absolute;left:0;top:2264px;width:1200px;height:293px;background:var(--dark);color:var(--white)}
.foot-title{position:absolute;font-size:30px;font-weight:500;color:var(--white)}
.foot-rule{position:absolute}
.contact-list{position:absolute;left:153px;top:125px;font-size:11px;line-height:18px;color:var(--foot-text)}
.contact-list li{list-style:none;display:flex;align-items:center;gap:18px;color:var(--foot-text)}
.contact-list svg{width:13px;height:13px;flex:none}
.foot-brand{position:absolute;left:540px;top:60px;width:120px;text-align:center;font-size:18px;font-weight:400;color:var(--white);line-height:22px}
.foot-brand .mark{width:60px;height:60px;border-radius:50%;background:var(--teal);margin:0 auto 10px}
.email-field{position:absolute;left:729px;top:125px;width:189px;height:33px;border:2px solid var(--white);font-size:14px;color:#ddd;padding:7px 12px}
.sub-btn{position:absolute;left:932px;top:125px;width:117px;height:33px}
.socials{position:absolute;left:730px;top:174px;display:flex;gap:14px}
.socials span{width:20px;height:20px;border:2px solid var(--white);border-radius:50%}
.copyright{position:absolute;left:0;width:1200px;top:225px;text-align:center;font-size:11px;color:#ddd}
</style>
</head>
<body>
<div class="page">

<header class="site-header">
  <div class="brand"><span class="brand-dot"></span>Ebbtide Haven</div>
  <nav class="main-nav"><span>HOME</span><span>FLOAT</span><span>IR SAUNA</span><span>MHBOT</span><span>BIOMAT</span><span>GIFT CARDS</span></nav>
  <div class="header-book btn-teal">BOOK NOW</div>
</header>

<section class="hero" role="img" aria-label="Bright spa lounge with teal sofa, round coffee table, plants and white curtains">
  <h1 class="hero-title">Wellness Spa</h1>
  <p class="hero-sub">Where the magic begins</p>
  <div class="hero-book">BOOK NOW</div>
</section>

<section class="about">
  <h2 class="section-title about-title">ABOUT US</h2>
  <div class="rule about-rule"></div>
  <h3 class="mission-head">Our Mission</h3>
  <p class="mission-text" style="top:846px">Our Mission Is To Provide A Purpose-Built Space For Our Clients To Relax, Recover And Optimise Their Health. Ebbtide Haven Offers Flotation Therapy, Mild Hyperbaric Oxygen Therapy (MHBOT), Infrared Sauna And Biomat Sessions.</p>
  <p class="mission-text" style="top:926px">To Help Us Serve And Provide Real Value To Our Clients We Offer Membership And Bulk Booking Discounts, As Well As Great Offers In-Store.</p>
  <div class="pod-frame"></div>
  <div class="pod-photo" role="img" aria-label="Closed white float pod"></div>
</section>

<section class="slider">
  <svg class="arrow" style="left:130px;top:1249px" viewBox="0 0 52 52" aria-hidden="true"><circle cx="26" cy="26" r="24" fill="none" stroke="#222" stroke-width="2.5"/><path d="M38 26H14M24 15L13 26l11 11" fill="none" stroke="#222" stroke-width="2.5"/></svg>
  <div class="slide-photo" role="img" aria-label="Open float tank with glowing blue water in a bright treatment room"></div>
  <div class="slide-panel">
    <h3>FLOAT TANK</h3>
    <p class="len">60 MIN</p>
    <p class="sess">EARLY SESSIONS<br>6AM – 9AM</p>
    <p class="sess">NORMAL SESSIONS<br>9AM – 5PM</p>
    <p class="sess">LATE SESSIONS<br>5PM-10PM</p>
    <p class="price">$65.00</p>
    <div class="slide-book">BOOK NOW</div>
  </div>
  <svg class="arrow" style="left:1005px;top:1241px" viewBox="0 0 52 52" aria-hidden="true"><circle cx="26" cy="26" r="24" fill="none" stroke="#222" stroke-width="2.5"/><path d="M14 26h24M28 15l11 11-11 11" fill="none" stroke="#222" stroke-width="2.5"/></svg>
</section>

<section class="gallery-section">
  <h2 class="section-title gallery-title">ABOUT US</h2>
  <div class="rule gallery-rule"></div>
  <div class="gallery">
    <div role="img" aria-label="Float pod lit in orange" style="background:radial-gradient(ellipse at 35% 45%,#ff4a12 0%,#ff6a22 45%,#f5a15a 80%,#f1d3b4 100%)"></div>
    <div role="img" aria-label="Aroma diffuser beside brochures and plant" style="background:radial-gradient(ellipse at 40% 75%,#d59a55 0%,#e7c79d 35%,#f1efea 70%,#e3e4e0 100%)"></div>
    <div role="img" aria-label="Float pod with blue interior" style="background:radial-gradient(ellipse at 65% 45%,#8fd0ea 0%,#b7dfee 35%,#ede9e2 70%,#d4cfc6 100%)"></div>
    <div role="img" aria-label="Reception desk with plants" style="background:radial-gradient(ellipse at 55% 60%,#ffffff 0%,#f2efe6 45%,#e6ddc6 80%,#c9c3b8 100%)"></div>
    <div role="img" aria-label="Infrared sauna cabin with blue mat" style="background:radial-gradient(ellipse at 50% 78%,#1ab0ea 0%,#3ab9e6 28%,rgba(0,0,0,0) 55%),linear-gradient(180deg,#d8b98c 0%,#5a4a3a 45%,#c79d68 100%)"></div>
    <div role="img" aria-label="Treatment bed and salt lamp" style="background:radial-gradient(ellipse at 40% 95%,#8d82c2 0%,#a59dc9 25%,rgba(0,0,0,0) 50%),linear-gradient(180deg,#f5f0e4 0%,#ece6da 55%,#c9c3ba 100%)"></div>
    <div role="img" aria-label="Glass jars and golden tea strainers" style="background:radial-gradient(ellipse at 50% 70%,#c08a3c 0%,#ddbe8a 40%,#eee6d6 75%,#c9c2b2 100%)"></div>
    <div role="img" aria-label="Lounge with sofa by curtained window" style="background:radial-gradient(ellipse at 25% 80%,#2c5e80 0%,rgba(44,94,128,0) 40%),linear-gradient(180deg,#f7f5ef 0%,#f1ede3 55%,#d9cfbd 100%)"></div>
  </div>
  <div class="show-more btn-teal">SHOW MORE</div>
</section>

<footer class="site-footer">
  <h2 class="foot-title" style="left:153px;top:55px">CONTACT US</h2>
  <div class="rule foot-rule" style="left:153px;top:100px"></div>
  <ul class="contact-list">
    <li><svg viewBox="0 0 12 12"><path d="M6 0a4 4 0 0 0-4 4c0 3 4 8 4 8s4-5 4-8a4 4 0 0 0-4-4zm0 5.5a1.5 1.5 0 1 1 0-3 1.5 1.5 0 0 1 0 3z" fill="#fff"/></svg>Unit 4, 118 Marlow Road, Kelsworth, QLD, 4512</li>
    <li><svg viewBox="0 0 12 12"><path d="M0 2h12v8H0z" fill="#fff"/><path d="M0 2l6 4 6-4" fill="none" stroke="#3f3f3f"/></svg><span>Admin@Ebbtidehaven.Com.Au</span></li>
    <li><svg viewBox="0 0 12 12"><path d="M2 0l2 3-1 1.5c.8 1.8 2.2 3.2 4 4L8.5 7.5l3 2-1 2.5C5 12 0 7 0 1.5z" fill="#fff"/></svg><span>1800 555 019</span></li>
  </ul>
  <div class="foot-brand"><div class="mark"></div>EBBTIDE HAVEN</div>
  <h2 class="foot-title" style="left:729px;top:55px">STAY IN THE ZONE</h2>
  <div class="rule foot-rule" style="left:729px;top:100px"></div>
  <div class="email-field">*Enter your email</div>
  <div class="sub-btn btn-teal">SHOW MORE</div>
  <div class="socials" aria-label="Social links"><span></span><span></span><span></span><span></span></div>
  <p class="copyright">© 2019 - Ebbtide Haven</p>
</footer>

</div>
</body>
</html>
```